Mental Health care Company in Washington DC

We are a new mental health care services provider in Washington DC. Please look at these sites.
https://marlowbrookpartners.com
https://www.quillstoneinc.com
https://velmarsh-kt.org/
https://www.trivanqx.com
https://www.thelanternofqz.com

```html
<!DOCTYPE html>
<html lang="en">
<head>
<meta charset="utf-8">
<title>Aster Health Services</title>
<link href="https://fonts.googleapis.com/css2?family=Poppins:wght@400;500;600;700&display=swap" rel="stylesheet">
<style>
:root{
  --navy:#0f1f44;
  --text:#3a4256;
  --muted:#6b7283;
  --orange:#f5a05a;
  --teal:#a9d9dc;
  --teal-soft:#e9f5f5;
  --peach:#fbe2cf;
  --white:#ffffff;
  --line:#e6e8ee;
  --footer-text:#c9cfdd;
}
*{box-sizing:border-box;margin:0;padding:0}
html,body{width:1200px;height:3818px;overflow:hidden}
body{font-family:'Poppins',sans-serif;color:var(--text);background:var(--white);position:relative}
.abs{position:absolute}
section,header,footer{position:absolute;left:0;width:1200px}
.btn{position:absolute;display:flex;align-items:center;justify-content:center;gap:6px;font-weight:600;border-radius:3px;font-size:11px;white-space:nowrap}
.btn-orange{background:var(--orange);color:var(--white)}
.btn-outline{border:1.5px solid var(--navy);color:var(--navy);background:var(--white)}
.center{text-align:center}
h2{font-weight:700;color:var(--navy)}

/* header */
.site-header{top:0;height:73px;background:var(--white);z-index:5}
.brand{position:absolute;left:162px;top:20px;color:var(--navy);font-size:28px;font-weight:600;line-height:1;letter-spacing:-.3px}
.nav a{position:absolute;top:28px;font-size:10.5px;color:var(--navy);text-decoration:none}

/* hero */
.hero{top:73px;height:531px;overflow:hidden}
.hero-photo{position:absolute;inset:0;background:linear-gradient(100deg,#f2f3f4 0%,#e7eaec 40%,#c8d7d4 60%,#b9c4b8 75%,#dde4e5 100%)}
.hero h1{position:absolute;left:162px;top:118px;font-size:40px;line-height:42px;color:var(--navy);font-weight:700}
.hero p{position:absolute;left:162px;top:222px;font-size:20px;line-height:26px;color:var(--navy)}

/* mission */
.mission{top:604px;height:400px}
.mission h2{position:absolute;top:50px;width:100%;font-size:24px}
.mission .lead{position:absolute;left:275px;width:650px;top:92px;font-size:11.5px;line-height:18px}
.pillar{position:absolute;top:180px;width:230px;text-align:center}
.pillar .ico{width:38px;height:38px;border-radius:50%;margin:0 auto 12px;display:flex;align-items:center;justify-content:center}
.pillar h3{font-size:13px;color:var(--navy);font-weight:600;margin-bottom:8px}
.pillar p{font-size:10px;line-height:15px;color:var(--muted)}

/* treat */
.treat{top:1004px;height:470px}
.treat-photo{position:absolute;left:156px;top:101px;width:272px;height:272px;border-radius:50%;background:linear-gradient(135deg,#d4d2cc,#8e9498 55%,#5f676b)}
.treat h2{position:absolute;left:526px;top:50px;font-size:24px}
.treat .lead{position:absolute;left:526px;top:96px;font-size:12px}
.cond{position:absolute;width:249px;height:70px;border:1px solid var(--line);border-radius:6px;background:var(--white);box-shadow:0 2px 6px rgba(15,31,68,.05)}
.cond .ci{position:absolute;left:12px;top:18px;width:32px;height:32px;border-radius:5px;display:flex;align-items:center;justify-content:center}
.cond h4{position:absolute;left:54px;top:17px;font-size:11px;color:var(--navy);font-weight:600;white-space:nowrap}
.cond p{position:absolute;left:54px;top:35px;width:185px;font-size:9.5px;line-height:13px;color:var(--muted)}

/* services */
.services{top:1474px;height:924px}
.services h2{position:absolute;top:50px;width:100%;font-size:24px}
.services .lead{position:absolute;top:99px;width:100%;font-size:13px}
.svc{position:absolute;width:276px;height:288px;background:var(--white);border-radius:4px;box-shadow:0 3px 10px rgba(15,31,68,.1);overflow:hidden}
.svc .ph{height:170px}
.svc .badge{position:absolute;left:24px;top:157px;width:26px;height:26px;border-radius:50%;background:var(--white);box-shadow:0 1px 4px rgba(0,0,0,.15);display:flex;align-items:center;justify-content:center}
.svc h3{position:absolute;left:24px;top:190px;width:240px;font-size:15px;line-height:20px;color:var(--navy);font-weight:600}
.svc p{position:absolute;left:24px;width:210px;font-size:11.5px;line-height:18px;color:var(--muted)}

/* quick access */
.quick{top:2398px;height:256px;background:linear-gradient(90deg,#2e2620 0%,#5b4b3f 40%,#9b7b5e 62%,#5a4538 80%,#2b221c 100%)}
.quick h2{position:absolute;top:62px;width:100%;color:var(--white);font-size:23px}
.qa{position:absolute;top:121px;width:166px;height:76px;background:var(--white);border-radius:3px;text-align:center;padding-top:16px;font-size:10.5px;font-weight:600;color:var(--navy)}
.qa svg{display:block;margin:0 auto 8px}

/* why */
.why{top:2654px;height:318px;background:var(--teal-soft);overflow:hidden}
.why h2{position:absolute;left:160px;top:30px;font-size:23px}
.why ul{position:absolute;left:160px;top:95px;list-style:none}
.why li{font-size:12px;color:var(--navy);height:33px;display:flex;align-items:center;gap:8px}
.journey{position:absolute;left:748px;top:52px;width:290px;height:192px;background:var(--white);border-radius:5px;box-shadow:0 3px 12px rgba(15,31,68,.1)}
.journey h3{position:absolute;left:20px;top:20px;font-size:15px;color:var(--navy);font-weight:600}
.journey p{position:absolute;left:20px;top:50px;width:252px;font-size:9.5px;line-height:15px;color:var(--muted)}

/* testimonials */
.testimonials{top:2972px;height:434px;background:linear-gradient(100deg,#f5e9dd 0%,#dfe6dc 50%,#a9d8d8 100%)}
.testimonials h2{position:absolute;top:68px;width:100%;font-size:24px}
.quote{position:absolute;top:135px;width:424px;height:157px;background:var(--white);border-radius:4px;box-shadow:0 3px 10px rgba(15,31,68,.08)}
.stars{position:absolute;left:20px;top:16px;color:var(--orange);font-size:13px;letter-spacing:1px}
.qmark{position:absolute;left:20px;top:34px;font-size:30px;color:#c9ccd4;font-family:Georgia,serif}
.quote p{position:absolute;left:20px;top:76px;width:380px;font-size:11.5px;line-height:18px}
.quote .who{top:122px;font-size:10px;font-weight:600;color:var(--navy)}

/* footer */
.site-footer{top:3406px;height:412px;background:var(--navy);color:var(--footer-text);overflow:hidden}
.site-footer .brand{left:162px;top:42px;color:var(--white);font-size:22px}
.f-about{position:absolute;left:162px;top:95px;width:300px;font-size:10px;line-height:16px}
.social{position:absolute;top:156px;width:14px;height:14px;border-radius:50%;border:1.5px solid var(--footer-text)}
.f-col h4{font-size:11px;color:var(--white);font-weight:600;margin-bottom:22px}
.f-col a,.f-col span{display:block;font-size:10px;line-height:20px;color:var(--footer-text);text-decoration:none}
.newsletter h4{position:absolute;top:226px;width:100%;font-size:11px;font-weight:600;color:var(--white)}
.newsletter p{position:absolute;top:255px;width:100%;font-size:10px}
.email-box{position:absolute;left:461px;top:282px;width:278px;height:24px;background:var(--white);border-radius:3px}
.email-box span{position:absolute;left:12px;top:5px;font-size:9px;color:#a0a6b3}
.email-box .send{position:absolute;right:0;top:0;width:40px;height:24px;background:var(--orange);border-radius:0 3px 3px 0;display:flex;align-items:center;justify-content:center}
.legal{position:absolute;width:100%;font-size:9.5px;text-align:center}
</style>
</head>
<body>

<header class="site-header">
  <div class="brand">Aster Health</div>
  <nav class="nav">
    <a style="left:409px">About Us</a>
    <a style="left:474px">Our Services</a>
    <a style="left:555px">Therapies &amp; Treatment</a>
    <a style="left:690px">For Clients</a>
    <a style="left:761px">Careers</a>
    <a style="left:820px">Contact Us</a>
  </nav>
  <div class="btn btn-orange" style="left:922px;top:22px;width:115px;height:25px;font-size:9.5px">Book Appointment</div>
</header>

<section class="hero">
  <div class="hero-photo" role="img" aria-label="Therapist holding a client's hands across a table in a bright clinic room"></div>
  <h1>Welcome to<br>Aster Health Services</h1>
  <p>Empowering lives through compassionate,<br>personalized mental health care.</p>
  <div class="btn btn-orange" style="left:162px;top:317px;width:216px;height:32px;font-size:11px">
    <svg width="11" height="11" viewBox="0 0 12 12" fill="none" stroke="#fff" stroke-width="1.3"><rect x="1.5" y="2.5" width="9" height="8" rx="1"/><path d="M1.5 5h9M4 1v3M8 1v3"/></svg>Book Your Appointment Today</div>
  <div class="btn btn-outline" style="left:401px;top:317px;width:158px;height:32px;font-size:11px;border-color:#fff">
    <svg width="11" height="11" viewBox="0 0 12 12" fill="none" stroke="#0f1f44" stroke-width="1.3"><path d="M2 1.5h2.5l1 3-1.5 1a6 6 0 0 0 2.5 2.5l1-1.5 3 1V10a1 1 0 0 1-1 1A9 9 0 0 1 1 2.5a1 1 0 0 1 1-1z"/></svg>Call: (202) 555-0148</div>
</section>

<section class="mission">
  <h2 class="center">Our Mission</h2>
  <p class="lead center">At Aster Health Services, we are committed to restoring hope and fostering healing for individuals and families in Washington, DC. Our person-centered approach focuses on whole-person wellness, evidence-based treatments, and culturally sensitive care.</p>
  <div class="pillar" style="left:192px">
    <div class="ico" style="background:var(--teal)"><svg width="18" height="18" viewBox="0 0 20 20" fill="none" stroke="#fff" stroke-width="1.6"><path d="M10 17s-7-4.3-7-9a4 4 0 0 1 7-2.5A4 4 0 0 1 17 8c0 4.7-7 9-7 9z"/></svg></div>
    <h3>Compassionate Care</h3>
    <p>Every individual deserves to be treated with dignity, respect, and understanding on their healing journey.</p>
  </div>
  <div class="pillar" style="left:491px">
    <div class="ico" style="background:var(--orange)"><svg width="18" height="18" viewBox="0 0 20 20" fill="none" stroke="#fff" stroke-width="1.6"><circle cx="8" cy="7" r="3"/><path d="M2 17a6 6 0 0 1 12 0M13 4a3 3 0 0 1 0 6M15 12a5 5 0 0 1 3 5"/></svg></div>
    <h3>Person-Centered Approach</h3>
    <p>We tailor our treatments to meet each client's unique needs, goals, and cultural background.</p>
  </div>
  <div class="pillar" style="left:777px">
    <div class="ico" style="background:var(--navy)"><svg width="18" height="18" viewBox="0 0 20 20" fill="none" stroke="#fff" stroke-width="1.6"><path d="M10 2l6 2.5V9c0 4-2.6 7-6 8.5C6.6 16 4 13 4 9V4.5z"/></svg></div>
    <h3>Evidence-Based Treatment</h3>
    <p>Our interventions are grounded in scientific research and proven therapeutic methodologies.</p>
  </div>
</section>

<section class="treat">
  <div class="treat-photo" role="img" aria-label="Young woman sitting with her head in her hands during a counseling session"></div>
  <h2>What We Treat</h2>
  <p class="lead">We help clients facing a wide range of mental health challenges:</p>
  <div class="cond" style="left:526px;top:133px"><div class="ci" style="background:var(--peach)"><svg width="16" height="16" viewBox="0 0 16 16" fill="none" stroke="#f5a05a" stroke-width="1.3"><circle cx="8" cy="8" r="6"/><path d="M8 3v10M5 6h6M5 10h6"/></svg></div><h4>Depression &amp; Anxiety</h4><p>Comprehensive treatment for mood disorders</p></div>
  <div class="cond" style="left:788px;top:133px"><div class="ci" style="background:var(--teal-soft)"><svg width="16" height="16" viewBox="0 0 16 16" fill="none" stroke="#6fc1c6" stroke-width="1.3"><path d="M8 14s-6-3.6-6-7.5A3.3 3.3 0 0 1 8 4.5a3.3 3.3 0 0 1 6 2c0 3.9-6 7.5-6 7.5z"/></svg></div><h4>Trauma &amp; PTSD</h4><p>Healing from traumatic experiences</p></div>
  <div class="cond" style="left:526px;top:216px"><div class="ci" style="background:var(--teal-soft)"><svg width="16" height="16" viewBox="0 0 16 16" fill="none" stroke="#6fc1c6" stroke-width="1.3"><circle cx="8" cy="8" r="6"/><path d="M8 3v10M5 6h6M5 10h6"/></svg></div><h4>Bipolar &amp; Mood Disorders</h4><p>Stabilizing mood fluctuations</p></div>
  <div class="cond" style="left:788px;top:216px"><div class="ci" style="background:var(--peach)"><svg width="16" height="16" viewBox="0 0 16 16" fill="none" stroke="#f5a05a" stroke-width="1.3"><circle cx="6" cy="6" r="2.5"/><path d="M1.5 14a4.5 4.5 0 0 1 9 0M10.5 3.5a2.5 2.5 0 0 1 0 5M12 10a4 4 0 0 1 2.5 4"/></svg></div><h4>Youth &amp; Family Conflict</h4><p>Strengthening family relationships</p></div>
  <div class="cond" style="left:526px;top:299px"><div class="ci" style="background:var(--peach)"><svg width="16" height="16" viewBox="0 0 16 16" fill="none" stroke="#f5a05a" stroke-width="1.3"><path d="M9 1L3 9h5l-1 6 6-8H8z"/></svg></div><h4>Substance Use Disorders</h4><p>Recovery and addiction support</p></div>
  <div class="cond" style="left:788px;top:299px"><div class="ci" style="background:var(--teal-soft)"><svg width="16" height="16" viewBox="0 0 16 16" fill="none" stroke="#6fc1c6" stroke-width="1.3"><path d="M2 5V2h3M11 2h3v3M14 11v3h-3M5 14H2v-3"/><circle cx="8" cy="8" r="2"/></svg></div><h4>ADHD &amp; Behavioral Challenges</h4><p>Managing attention and behavior</p></div>
  <div class="btn btn-outline" style="left:526px;top:393px;width:215px;height:31px;font-size:8.5px">Learn More About Conditions We Treat →</div>
</section>

<section class="services">
  <h2 class="center">Our Services</h2>
  <p class="lead center">Comprehensive Mental Health Support, We offer a full range of outpatient services:</p>

  <div class="svc" style="left:163px;top:152px"><div class="ph" role="img" aria-label="Young women talking together in a bright room with plants" style="background:linear-gradient(135deg,#c9c3ba,#8f8a82 60%,#6f7a66)"></div><div class="badge"><svg width="14" height="14" viewBox="0 0 16 16" fill="none" stroke="#6fc1c6" stroke-width="1.3"><circle cx="8" cy="8" r="6"/><path d="M8 3v10M5 6h6M5 10h6"/></svg></div><h3>Psychiatric Services</h3><p style="top:226px">Medication Management &amp; Psychiatric Evaluations</p></div>
  <div class="svc" style="left:462px;top:152px"><div class="ph" role="img" aria-label="Therapist listening to a client in a study with bookshelves" style="background:linear-gradient(135deg,#b88a66,#6f5b4c 50%,#c7c4bd)"></div><div class="badge"><svg width="14" height="14" viewBox="0 0 16 16" fill="none" stroke="#f5a05a" stroke-width="1.3"><path d="M2 13l1-3a5.5 5.5 0 1 1 2 2z"/></svg></div><h3>Individual Therapy</h3><p style="top:217px">1:1 sessions with licensed professionals</p></div>
  <div class="svc" style="left:761px;top:152px"><div class="ph" role="img" aria-label="Couple on a sofa speaking with a counselor in a living room" style="background:linear-gradient(135deg,#d8d4cc,#8a7360 55%,#4f4741)"></div><div class="badge"><svg width="14" height="14" viewBox="0 0 16 16" fill="none" stroke="#0f1f44" stroke-width="1.3"><circle cx="6" cy="6" r="2.5"/><path d="M1.5 14a4.5 4.5 0 0 1 9 0M10.5 3.5a2.5 2.5 0 0 1 0 5M12 10a4 4 0 0 1 2.5 4"/></svg></div><h3>Family &amp; Couples Therapy</h3><p style="top:219px">Strengthen bonds, rebuild relationships</p></div>

  <div class="svc" style="left:163px;top:472px"><div class="ph" role="img" aria-label="Group of people joining hands at a support meeting" style="background:linear-gradient(135deg,#6b4a3c,#8a6c9c 45%,#c6a488)"></div><div class="badge"><svg width="14" height="14" viewBox="0 0 16 16" fill="none" stroke="#6fc1c6" stroke-width="1.3"><circle cx="8" cy="8" r="6"/><circle cx="8" cy="7" r="2"/><path d="M4.5 12.5a4 4 0 0 1 7 0"/></svg></div><h3>Community Support<br>Services (CSS)</h3><p style="top:236px;width:240px">Re-engage with life, work, and purpose</p></div>
  <div class="svc" style="left:462px;top:472px"><div class="ph" role="img" aria-label="Teenagers seated in a circle for a group session" style="background:linear-gradient(135deg,#d9d6cf,#9a8a7c 50%,#6e7f88)"></div><div class="badge"><svg width="14" height="14" viewBox="0 0 16 16" fill="none" stroke="#f5a05a" stroke-width="1.3"><path d="M1 6l7-3 7 3-7 3z"/><path d="M4 8v3c2 2 6 2 8 0V8"/></svg></div><h3>Youth Counseling &amp;<br>School-Based Programs</h3><p style="top:236px">Empowering future generations</p></div>
  <div class="svc" style="left:761px;top:472px"><div class="ph" role="img" aria-label="Stressed man at a laptop with colleagues offering help" style="background:linear-gradient(135deg,#c9a277,#3b3a3e 50%,#e4e3e2)"></div><div class="badge"><svg width="14" height="14" viewBox="0 0 16 16" fill="none" stroke="#0f1f44" stroke-width="1.3"><path d="M8 2L1.5 13.5h13z"/><path d="M8 6.5v3.5M8 11.5v.5"/></svg></div><h3>Crisis Intervention &amp; Case Management</h3><p style="top:236px">Help when you need it most</p></div>

  <div class="btn btn-orange" style="left:527px;top:813px;width:145px;height:31px;font-size:11px">View All Services →</div>
</section>

<section class="quick" role="img" aria-label="Blurred background photo of a woman on the phone">
  <h2 class="center">Quick Access</h2>
  <div class="qa" style="left:160px"><svg width="16" height="16" viewBox="0 0 16 16" fill="none" stroke="#a9d9dc" stroke-width="1.3"><path d="M3 1.5h7l3 3v10H3z"/><path d="M5.5 8h5M5.5 11h5"/></svg>Download Intake Forms</div>
  <div class="qa" style="left:338px"><svg width="16" height="16" viewBox="0 0 16 16" fill="none" stroke="#f5a05a" stroke-width="1.3"><rect x="2" y="3" width="12" height="11" rx="1"/><path d="M2 7h12M5 1.5v3M11 1.5v3"/></svg>Book Appointment</div>
  <div class="qa" style="left:517px"><svg width="16" height="16" viewBox="0 0 16 16" fill="none" stroke="#0f1f44" stroke-width="1.3"><path d="M2.5 1.5h3l1 3.5-1.8 1.2a8 8 0 0 0 3.6 3.6L9.5 8l3.5 1v3a1.5 1.5 0 0 1-1.5 1.5A11 11 0 0 1 1 3a1.5 1.5 0 0 1 1.5-1.5z"/></svg>(202) 555-0148</div>
  <div class="qa" style="left:695px"><svg width="16" height="16" viewBox="0 0 16 16" fill="none" stroke="#a9d9dc" stroke-width="1.3"><rect x="1.5" y="4.5" width="13" height="9" rx="1"/><path d="M5.5 4.5v-2h5v2M5.5 4.5v9M10.5 4.5v9"/></svg>Join Our Team</div>
  <div class="qa" style="left:872px"><svg width="16" height="16" viewBox="0 0 16 16" fill="none" stroke="#0f1f44" stroke-width="1.3"><rect x="1.5" y="3" width="13" height="10" rx="1"/><path d="M1.5 4l6.5 5 6.5-5"/></svg>hello@asterhealth.org</div>
</section>

<section class="why">
  <h2>Why Choose Aster?</h2>
  <ul>
    <li><svg width="13" height="13" viewBox="0 0 14 14" fill="none" stroke="#8fd0c8" stroke-width="1.3"><circle cx="7" cy="7" r="6"/><path d="M4.3 7.2l1.9 1.8 3.6-3.8"/></svg>Licensed, Experienced Clinicians</li>
    <li><svg width="13" height="13" viewBox="0 0 14 14" fill="none" stroke="#8fd0c8" stroke-width="1.3"><circle cx="7" cy="7" r="6"/><path d="M4.3 7.2l1.9 1.8 3.6-3.8"/></svg>Medicaid &amp; Major Insurances Accepted</li>
    <li><svg width="13" height="13" viewBox="0 0 14 14" fill="none" stroke="#8fd0c8" stroke-width="1.3"><circle cx="7" cy="7" r="6"/><path d="M4.3 7.2l1.9 1.8 3.6-3.8"/></svg>No One Denied for Inability to Pay</li>
    <li><svg width="13" height="13" viewBox="0 0 14 14" fill="none" stroke="#8fd0c8" stroke-width="1.3"><circle cx="7" cy="7" r="6"/><path d="M4.3 7.2l1.9 1.8 3.6-3.8"/></svg>Multilingual &amp; Culturally Competent Care</li>
    <li><svg width="13" height="13" viewBox="0 0 14 14" fill="none" stroke="#8fd0c8" stroke-width="1.3"><circle cx="7" cy="7" r="6"/><path d="M4.3 7.2l1.9 1.8 3.6-3.8"/></svg>Safe, Inclusive, Confidential Space</li>
  </ul>
  <div class="journey">
    <h3>Ready to Begin Your Journey?</h3>
    <p>Take the first step towards better mental health. Our compassionate team is here to support you every step of the way.</p>
    <div class="btn btn-orange" style="left:20px;top:122px;width:250px;height:23px;font-size:8.5px">Schedule Your Appointment</div>
    <div class="btn btn-outline" style="left:20px;top:153px;width:250px;height:23px;font-size:8.5px;border-width:1px">Call (202) 555-0148</div>
  </div>
</section>

<section class="testimonials">
  <h2 class="center">Testimonials</h2>
  <div class="quote" style="left:163px"><div class="stars">★★★★★</div><div class="qmark">“</div><p>"Aster Health Services changed my life. I feel seen, heard, and supported every step of the way."</p><p class="who">– A.C., Client</p></div>
  <div class="quote" style="left:613px"><div class="stars">★★★★★</div><div class="qmark">“</div><p>"Their team really cares about mental health. My child is thriving at school again."</p><p class="who">– T.S., Parent</p></div>
  <div class="btn btn-outline" style="left:533px;top:334px;width:134px;height:31px;font-size:9px">Read More Stories →</div>
</section>

<footer class="site-footer">
  <div class="brand">Aster Health</div>
  <p class="f-about">Empowering lives through compassionate, personalized mental health care in Washington, DC. Your Mind Matters. Your Wellness Begins Here.</p>
  <span class="social" style="left:169px"></span><span class="social" style="left:203px"></span><span class="social" style="left:238px"></span>
  <div class="f-col abs" style="left:675px;top:54px"><h4>Quick Links</h4><a>Home</a><a>About Us</a><a>Our Services</a><a>Contact</a></div>
  <div class="f-col abs" style="left:900px;top:54px"><h4>Contact</h4><span>(202) 555-0148</span><span>hello@asterhealth.org</span><span style="line-height:14px">880 Harbor Lane, Suite 210<br>Washington, DC 20000</span></div>
  <div class="newsletter"><h4 class="center">Stay Connected</h4><p class="center">Subscribe to our newsletter for updates &amp; resources.</p></div>
  <div class="email-box"><span>Enter your email</span><div class="send"><svg width="13" height="13" viewBox="0 0 16 16" fill="none" stroke="#fff" stroke-width="1.4"><rect x="1.5" y="3" width="13" height="10" rx="1"/><path d="M1.5 4l6.5 5 6.5-5"/></svg></div></div>
  <p class="legal" style="top:357px">© 2025 Aster Health Services | Washington, DC | All rights reserved</p>
  <p class="legal" style="top:382px">Privacy Policy &nbsp; Accessibility &nbsp; Site Map</p>
</footer>

</body>
</html>
```